Gourmet food company looking for a dazzling label for their premuim vinagrette dressings

Need a food label that will dazzle our customer and prove what a premium product we have. We make high end gourmet dressing for vegetables, fruit, meat, poultry and fish.

Our label will fit on a 250 mil Tolvenna Square bottle. Labels should be a 4x5 or even 5x5 depending on the design. Nutritionals, bar codes and company blurb will be supplied later. We really want to test you all's talent on this one and are very excited to see your renderings!

Our dressings are Champagne Pear Vinaigrette, White Balsmic Vinaigrette, Mojito Lime Vinaigrette, Creamy-Avacado Lime Vinaigrette, and Asian Sesame Vinaigrette. I hope these names will help you envision our product and kinda what we are looking for.

Thank you all so far for your renderings.I really don't want pictures if that helps. Our logo can be smaller and/or the name of the product bigger. Perhaps we can even redesign Lumora and remove the leaf as I don't really care for what I see yet.So good luck and thanks Added Friday, August 19, 2016

I am still looking for that clean - elegant design for our product as our product is just that. If you look on the internet at vinegars and oils you will see many designs that are simple yet elegant. Creative lettering, bordering, color (can be black and white) and size will help accomplish this. So I invite you to use all your creativity and help me find just what we need.Many thanks Added Tuesday, August 23, 2016

Project Deadline Extended Reason: So many great designs coming in that I wanted a few extra days to tweek!Great job all Added Friday, August 26, 2016

Project Deadline Extended Reason: Very good designs thus far. We just need a few more days.Thanks Added Wednesday, August 31, 2016

Target Market(s)

High end grocery and specialty stores.

Our side panel on the label will say "At Lumora we're fanatics for great flavors and are passionate about finding the best ingredients. From simple to elegant our products are "simply lumora".

Industry/Entity Type

It Company

Font styles to use
Serif
Decorative
Script

Requirements
Must have
• A label that will draw the consumer to pick it up! Need something bold and elegant...
Nice to have
• Again, I really would like to have a label that pops. Since the bottle front is only about 2inches in width it will need some creativity. Would like something very simple and elegant.
• If the designer does not like the logo, please feel free to design without it!
Should not have
• Dark dark colors. We are selling dressing and we don't want any colors that may distort the contents.
• No stock photos for the front. I don't want our dressing to look like the others on the self. Brackwell Pantry just uses lettering and a their packaging is eye catching

```html
<!DOCTYPE html>
<html lang="en">
<head>
<meta charset="utf-8">
<title>Lumora Champagne Pear Vinaigrette Label</title>
<link href="https://fonts.googleapis.com/css2?family=Pinyon+Script&family=Lora:ital,wght@0,500;1,400;1,700&display=swap" rel="stylesheet">
<style>
  :root {
    --cream: #f8f2e6;
    --band: #dcdedd;
    --ink: #141414;
    --plum: #2a1a2a;
    --brand-brown: #3b1d16;
    --panel-white: #ffffff;
    --panel-grey: #8e8e8e;
    --frame: #1a1a1a;
    --rule: #6a6a6a;
  }
  * { margin: 0; padding: 0; box-sizing: border-box; }
  html, body { width: 1200px; height: 971px; overflow: hidden; background: var(--cream); }
  .label { position: relative; width: 1200px; height: 971px; background: var(--cream); overflow: hidden; }

  .frame {
    position: absolute; left: 28px; top: 34px; width: 1146px; height: 901px;
    border: 3px solid var(--frame); z-index: 4; pointer-events: none;
  }

  .band {
    position: absolute; left: 32px; top: 363px; width: 1146px; height: 333px;
    background: var(--band);
    box-shadow: 0 22px 30px rgba(90, 70, 60, 0.35);
    z-index: 1;
  }
  .band-flourish {
    position: absolute; left: 64px; top: 368px; width: 200px; height: 328px;
    background: radial-gradient(ellipse at 50% 50%, rgba(170,170,170,0.45), rgba(220,222,221,0) 70%);
    z-index: 2;
  }

  .intro-script {
    position: absolute; left: 58px; top: 192px; width: 340px;
    font-family: "Pinyon Script", cursive;
    font-size: 45px; line-height: 46px; color: var(--plum);
    -webkit-text-stroke: 0.9px var(--plum);
    z-index: 3;
  }

  .brand {
    position: absolute; left: 430px; top: 166px; width: 340px; text-align: center; z-index: 3;
  }
  .brand-mark {
    display: block; width: 22px; height: 22px; border-radius: 50%;
    background: var(--brand-brown); margin: 0 auto 10px;
  }
  .brand-name {
    font-family: "Lora", serif; font-weight: 500;
    font-size: 84px; line-height: 84px; color: var(--brand-brown);
  }

  .story {
    position: absolute; left: 74px; top: 428px; width: 320px;
    font-family: "Lora", serif; font-style: italic; font-weight: 400;
    font-size: 22px; line-height: 32px; color: var(--ink);
    letter-spacing: 0.6px; z-index: 3; white-space: nowrap;
  }
  .story strong { font-weight: 700; }

  .product-name {
    position: absolute; left: 396px; top: 408px; width: 408px; text-align: center;
    font-family: "Pinyon Script", cursive; font-weight: 400; color: var(--ink); z-index: 3;
    -webkit-text-stroke: 0.9px var(--ink);
  }
  .product-flavour { display: block; font-size: 60px; line-height: 62px; }
  .product-type { display: block; font-size: 100px; line-height: 90px; -webkit-text-stroke: 1.6px var(--ink); }

  .divider {
    position: absolute; left: 404px; top: 586px; width: 386px; height: 76px; z-index: 3;
  }

  .info-panel {
    position: absolute; left: 858px; top: 226px; width: 276px; height: 494px;
    background: var(--panel-white); z-index: 3;
  }
  .info-panel .slot {
    position: absolute; left: 23px; top: 48px; width: 227px; height: 411px; background: var(--panel-grey);
  }
  .code-panel {
    position: absolute; left: 890px; top: 732px; width: 211px; height: 118px;
    background: var(--panel-white); z-index: 3;
  }
  .code-panel .slot {
    position: absolute; left: 16px; top: 10px; width: 180px; height: 101px; background: var(--panel-grey);
  }

  .claims {
    position: absolute; left: 420px; top: 806px; width: 360px; text-align: center;
    font-family: "Lora", serif; font-style: italic; color: var(--ink);
    text-shadow: 0 14px 14px rgba(90,70,60,0.25); z-index: 3;
  }
  .claims .natural { font-weight: 700; font-size: 31px; line-height: 36px; letter-spacing: 0.8px; }
  .claims .volume { font-weight: 400; font-size: 24px; line-height: 32px; letter-spacing: 0.8px; }
</style>
</head>
<body>
<main class="label">
  <div class="band"></div>
  <div class="band-flourish" role="img" aria-label="Faint decorative swirl flourish"></div>

  <p class="intro-script">At Lumora, we’re<br>fanatics for great<br>flavours...</p>

  <header class="brand">
    <span class="brand-mark"></span>
    <div class="brand-name">Lumora</div>
  </header>

  <p class="story">... and are passionate<br>about finding the <strong>best</strong><br><strong>ingredients.</strong> From simple<br>to elegant our products<br>are <strong>“simply lumora”</strong>.</p>

  <h1 class="product-name">
    <span class="product-flavour">Champagne Pear</span>
    <span class="product-type">Vinaigrette</span>
  </h1>

  <svg class="divider" viewBox="0 0 386 76">
    <defs>
      <radialGradient id="flourishTone" cx="50%" cy="50%" r="50%">
        <stop offset="0%" stop-color="#1a1a1a" stop-opacity="0.55"/>
        <stop offset="100%" stop-color="#1a1a1a" stop-opacity="0"/>
      </radialGradient>
    </defs>
    <line x1="0" y1="38" x2="84" y2="38" stroke="var(--rule)" stroke-width="1"/>
    <line x1="298" y1="38" x2="386" y2="38" stroke="var(--rule)" stroke-width="1"/>
    <rect x="100" y="4" width="186" height="68" fill="url(#flourishTone)" role="img" aria-label="Black calligraphic flourish ornament"/>
  </svg>

  <section class="info-panel"><div class="slot"></div></section>
  <section class="code-panel"><div class="slot"></div></section>

  <footer class="claims">
    <div class="natural">All Natural</div>
    <div class="volume">net weight: 8.5 fl oz</div>
  </footer>

  <div class="frame"></div>
</main>
</body>
</html>
```